Varnel Solutions requires a new business card.

We are an online professional tool store.

Target Market(s)

We target the professional technician.

Industry/Entity Type

Business

Contact Information for Business Card

VarnelSolutions.com.au

sales@varnelsolutions.com

Requirements
Must have
• Needs to look commercial and professional
Should not have
• No Australian Colors, maps or shapes.
• No Shapes of Tools

```html
<!DOCTYPE html>
<html lang="en">
<head>
<meta charset="utf-8">
<title>Varnel Solutions – Business Card</title>
<link href="https://fonts.googleapis.com/css2?family=Lato:wght@400;700&display=swap" rel="stylesheet">
<style>
  :root {
    --backdrop: #2a2a2c;
    --card-black: #1f1f21;
    --card-white: #f3f3f4;
    --emboss-grey: #55565a;
    --brand-blue: #3a4aa0;
    --accent-cyan: #2aa3c4;
    --text-dark: #2b2b2e;
    --text-grey: #4a4a4e;
    --band-text: #ffffff;
  }
  * { margin: 0; padding: 0; box-sizing: border-box; }
  html, body { width: 1200px; height: 716px; overflow: hidden; }
  body {
    background: var(--backdrop);
    font-family: "Lato", sans-serif;
    position: relative;
  }
  .card {
    position: absolute;
    width: 520px;
    height: 297px;
    top: 210px;
    overflow: hidden;
  }
  /* Back side */
  .card-back { left: 50px; background: var(--card-black); }
  .card-back .brand {
    position: absolute;
    left: 0; right: 0; top: 108px;
    display: flex; align-items: center; justify-content: center; gap: 12px;
    color: var(--emboss-grey);
  }
  .brand-dot {
    width: 30px; height: 30px; border-radius: 50%;
    background: currentColor;
  }
  .brand-name { font-weight: 700; font-size: 34px; letter-spacing: 0.5px; }
  .card-back .site {
    position: absolute; left: 0; right: 0; top: 178px;
    text-align: center; font-size: 13px; color: var(--emboss-grey);
    letter-spacing: 0.5px;
  }
  /* Front side */
  .card-front { left: 630px; background: var(--card-white); }
  .card-front .brand {
    position: absolute; left: 36px; top: 92px;
    display: flex; align-items: center; gap: 10px;
    color: var(--brand-blue);
  }
  .card-front .brand-dot { width: 26px; height: 26px; }
  .card-front .brand-name { font-size: 27px; }
  .contact {
    position: absolute; left: 318px; top: 78px;
  }
  .contact .person-name { font-size: 25px; color: var(--text-dark); font-weight: 400; }
  .contact .job-title { font-size: 14px; color: var(--brand-blue); margin-top: 2px; }
  .contact .line {
    display: flex; align-items: center; gap: 8px;
    font-size: 15px; color: var(--text-grey); margin-top: 14px;
  }
  .contact .line + .line { margin-top: 10px; }
  .contact svg { width: 16px; height: 16px; fill: var(--brand-blue); flex: none; }
  .band {
    position: absolute; left: 0; bottom: 30px;
    width: 430px; height: 30px;
    background: var(--brand-blue);
    display: flex; align-items: center; justify-content: space-between;
    padding: 0 14px 0 22px;
    color: var(--band-text); font-size: 14px;
  }
  .band .social { display: flex; align-items: center; gap: 8px; }
  .band .social-mark { width: 12px; height: 12px; background: var(--band-text); opacity: 0.85; }
  .accent-block {
    position: absolute; left: 440px; bottom: 30px;
    width: 80px; height: 30px; background: var(--accent-cyan);
  }
</style>
</head>
<body>
  <section class="card card-back" aria-label="Business card back">
    <div class="brand">
      <span class="brand-dot"></span>
      <span class="brand-name">Varnel Solutions</span>
    </div>
    <p class="site">VarnelSolutions.com.au</p>
  </section>

  <section class="card card-front" aria-label="Business card front">
    <div class="brand">
      <span class="brand-dot"></span>
      <span class="brand-name">Varnel Solutions</span>
    </div>
    <div class="contact">
      <p class="person-name">Your Name</p>
      <p class="job-title">Jobtile</p>
      <p class="line">
        <svg viewBox="0 0 24 24" aria-hidden="true"><path d="M6.6 10.8a15.1 15.1 0 0 0 6.6 6.6l2.2-2.2c.3-.3.7-.4 1-.2 1.1.4 2.3.6 3.6.6.6 0 1 .4 1 1V20c0 .6-.4 1-1 1A17 17 0 0 1 3 4c0-.6.4-1 1-1h3.5c.6 0 1 .4 1 1 0 1.3.2 2.5.6 3.6.1.3 0 .7-.2 1z"/></svg>
        000 000 0000
      </p>
      <p class="line">
        <svg viewBox="0 0 24 24" aria-hidden="true"><path d="M2 5h20v14H2z M3.5 6.5 12 13l8.5-6.5" fill="none" stroke="#3a4aa0" stroke-width="2"/></svg>
        youremail@xyz.com
      </p>
    </div>
    <div class="band">
      <span class="social"><span class="social-mark"></span>/varnelsolutions</span>
      <span class="site-link">VarnelSolutions.com.au</span>
    </div>
    <div class="accent-block"></div>
  </section>
</body>
</html>
```